Supplement Company looking for product design on a pre-work out and capsule supplement!

We are a small health supplement company that is making health supplements for competitive runners who are looking to increase their endurance. We have the utmost confidence in your ability to produce the best result. The designs sought are for our Pre-Workout supplement called "Kestro Surge-Up" that will be in a 12 oz plastic jar that comes in a and a Sodium Phosphate capsules called "Kestro VX" that will be in a bottle that holds 75 small capsules. We are looking for an amazing design for these products that is simple, and to the point. There are a lot of examples of different products that you can search such as Torvane Strak7, Z9 Pre-workout, UltrA-Sol Multivitamin, and Quillfen Nutrition products.
We do not have a photo of the product because we are looking for your design abilities to make the packaging design come to life on the product. The products should have the same design, same base color (silver), and the individual product colors (Green for Surge-Up and the Turquoise for SP).

Target Market(s)

Competitive Runners

Industry/Entity Type

Health And Wellness

Colors
ffffff
9bcb3c
87cfc6

Requirements
Must have
• A design of each product as to how it would appear in person. Including "Kestro Surge-Up" for the pre-workout and "Kestro VX" for the pills
• Must say "Dietary Supplement," in small print to the bottom left and "Zero banned substances" next to it.
• "Miles of energy, focus, and endurance" for the pre-workout or something to that effect (We are interested to see what else could be supplemented (no pun intended) in place of the word mix).
• The, "KL" from the logo uploaded in somewhere on the top left of the corner of the product.
Nice to have
• Transparent background, product only image that would allow the product to standout and the background on a website to stand without interference.
Should not have
• Colors outside of silver and whatever product color that is designated.

```html
<!DOCTYPE html>
<html lang="en">
<head>
<meta charset="utf-8">
<title>Kestro Surge-Up – Label</title>
<link href="https://fonts.googleapis.com/css2?family=Cinzel:wght@600;700&family=Montserrat:wght@600;700&display=swap" rel="stylesheet">
<style>
  :root {
    --page: #ffffff;
    --green: #1f7a2c;
    --green-deep: #135a1c;
    --green-light: #2e9a3c;
    --lime: #9bcb3c;
    --silver-light: #f2f2f2;
    --silver: #c9c9c9;
    --silver-dark: #8d8d8d;
    --ink: #0d0d0d;
    --white: #ffffff;
  }
  html, body {
    margin: 0;
    width: 1200px;
    height: 903px;
    overflow: hidden;
    background: var(--page);
  }
  .label {
    position: absolute;
    left: 120px;
    top: 190px;
    width: 960px;
    height: 520px;
    overflow: hidden;
    font-family: "Montserrat", sans-serif;
  }
  .label-art {
    position: absolute;
    inset: 0;
  }
  .brand-box {
    position: absolute;
    left: 26px;
    top: 20px;
    width: 200px;
    height: 96px;
    display: flex;
    flex-direction: column;
    align-items: center;
    justify-content: center;
    gap: 6px;
  }
  .brand-name {
    color: var(--lime);
    font-weight: 700;
    font-size: 30px;
    letter-spacing: 1px;
    line-height: 1;
  }
  .brand-sub {
    color: var(--lime);
    font-weight: 700;
    font-size: 11px;
    letter-spacing: 2px;
    line-height: 1;
  }
  .product-name {
    position: absolute;
    left: 0;
    right: 0;
    top: 165px;
    margin: 0;
    text-align: center;
    font-family: "Cinzel", serif;
    font-weight: 700;
    font-size: 76px;
    line-height: 1;
    color: var(--ink);
    -webkit-text-stroke: 1.5px var(--silver-light);
    letter-spacing: 1px;
    white-space: nowrap;
  }
  .tagline {
    position: absolute;
    left: 0;
    right: 0;
    top: 262px;
    margin: 0;
    text-align: center;
    color: var(--white);
    font-weight: 700;
    font-size: 24px;
    letter-spacing: 1px;
    line-height: 1.3;
  }
  .tagline-line {
    display: block;
  }
  .tagline-rule {
    display: inline-block;
    width: 60px;
    height: 2px;
    background: var(--white);
    vertical-align: middle;
    margin: 0 10px;
  }
  .claims {
    position: absolute;
    right: 36px;
    top: 412px;
    display: flex;
    gap: 18px;
    color: var(--white);
    font-weight: 600;
    font-size: 15px;
    letter-spacing: 1px;
    line-height: 1;
    white-space: nowrap;
  }
  .net-weight {
    position: absolute;
    right: 36px;
    top: 472px;
    color: var(--white);
    font-weight: 600;
    font-size: 17px;
    letter-spacing: 1px;
    line-height: 1;
  }
</style>
</head>
<body>
  <section class="label" aria-label="Kestro Surge-Up dietary supplement label">
    <svg class="label-art" width="960" height="520" viewBox="0 0 960 520">
      <defs>
        <linearGradient id="greenField" x1="0" y1="0" x2="1" y2="1">
          <stop offset="0" stop-color="#2e9a3c"/>
          <stop offset="0.55" stop-color="#1f7a2c"/>
          <stop offset="1" stop-color="#135a1c"/>
        </linearGradient>
        <linearGradient id="silverField" x1="0" y1="0" x2="1" y2="1">
          <stop offset="0" stop-color="#f2f2f2"/>
          <stop offset="0.5" stop-color="#c9c9c9"/>
          <stop offset="1" stop-color="#f2f2f2"/>
        </linearGradient>
        <linearGradient id="silverTrim" x1="0" y1="0" x2="1" y2="0">
          <stop offset="0" stop-color="#8d8d8d"/>
          <stop offset="0.5" stop-color="#f2f2f2"/>
          <stop offset="1" stop-color="#8d8d8d"/>
        </linearGradient>
      </defs>

      <rect class="green-field" width="960" height="520" fill="url(#greenField)"/>

      <g class="top-panel">
        <path d="M250 0 L960 0 L960 150 C760 150 520 120 250 0 Z" fill="url(#silverField)" role="img" aria-label="Perforated silver texture panel"/>
        <path d="M250 0 C520 120 760 150 960 150" fill="none" stroke="url(#silverTrim)" stroke-width="8"/>
      </g>

      <g class="bottom-panel">
        <path d="M0 380 C240 385 470 440 600 520 L0 520 Z" fill="url(#silverField)" role="img" aria-label="Perforated silver texture panel"/>
        <path d="M0 380 C240 385 470 440 600 520" fill="none" stroke="url(#silverTrim)" stroke-width="8"/>
        <path d="M520 450 L960 450" stroke="url(#silverTrim)" stroke-width="4"/>
        <path d="M620 508 L960 508" stroke="url(#silverTrim)" stroke-width="4"/>
      </g>

      <g class="brand-frame">
        <rect x="22" y="16" width="208" height="104" fill="#1f7a2c" stroke="url(#silverTrim)" stroke-width="5"/>
      </g>
    </svg>

    <div class="brand-box">
      <span class="brand-name">KESTRO</span>
      <span class="brand-sub">NUTRITION</span>
    </div>

    <h1 class="product-name">KESTRO SURGE-UP</h1>

    <p class="tagline">
      <span class="tagline-line">MILES OF ENERGY, FOCUS</span>
      <span class="tagline-line"><span class="tagline-rule"></span>AND ENDURANCE<span class="tagline-rule"></span></span>
    </p>

    <div class="claims">
      <span class="claim">DIETARY SUPPLEMENT</span>
      <span class="claim">ZERO BANNED SUBSTANCES</span>
    </div>
    <span class="net-weight">12 OZ / 340.19 GM</span>
  </section>
</body>
</html>
```